Packaging Sleeve Design for Yoghurt Tubs

Woofloma makes frozen yoghurt treats for dogs. Our healthy treats are packaged like regular yoghurt in small tubs with a lid.

What we require is a design for our packaging using all the current logos and flavor icons we already have available.

The packaging will be a carton sleeve that wraps around the tubs.

We would like to maintain a wholesome / homemade look about the packaging following the design and look of our existing logo. You can visit the website www.woofloma-example.com.au to get a better idea.

The packets will be displayed in a freezer so we would like something that will stand out to catch the customers eye.

Target Market(s)

Dog lovers, pet owners

Requirements
Must have
• Logo & flavours
All natural message
Low fat, low calories

```html
<!DOCTYPE html>
<html lang="en">
<head>
<meta charset="utf-8">
<title>Woofloma – Bibi Apple Sleeve</title>
<link rel="stylesheet" href="https://fonts.googleapis.com/css2?family=Delius&family=Oswald:wght@500;700&family=Open+Sans:wght@400&display=swap">
<style>
  :root {
    --sleeve-teal: #8fcdbd;
    --sleeve-teal-dark: #7dbfae;
    --ink: #262626;
    --white: #ffffff;
    --cream: #f6f1d9;
    --label-white: #fbfbfb;
    --photo-red: #7a1d22;
    --photo-dark: #3b0c10;
    --brand-dark: #2e2e2e;
  }
  * { box-sizing: border-box; margin: 0; padding: 0; }
  html, body { width: 1200px; height: 800px; overflow: hidden; background: var(--white); }
  .canvas { position: relative; width: 1200px; height: 800px; }

  /* Brand mark area, top right */
  .brand-mark {
    position: absolute; left: 800px; top: 170px; width: 340px; height: 100px;
    display: flex; align-items: center; justify-content: center; gap: 16px;
  }
  .brand-mark__dot { width: 26px; height: 26px; border-radius: 50%; background: var(--brand-dark); }
  .brand-mark__name {
    font-family: "Delius", cursive; font-size: 54px; color: var(--brand-dark);
  }

  /* Flat sleeve */
  .sleeve {
    position: absolute; left: 100px; top: 395px; width: 740px; height: 340px;
    background: var(--cream); border-radius: 6px; padding: 0 14px;
  }
  .sleeve__top, .sleeve__front { position: relative; background: var(--sleeve-teal); }
  .sleeve__top { height: 140px; border-bottom: 2px dotted var(--white); }
  .sleeve__front { height: 200px; }

  .top-brand {
    position: absolute; left: 30px; top: 40px;
    font-family: "Delius", cursive; font-size: 26px; color: var(--brand-dark);
  }
  .lid-label {
    position: absolute; left: 285px; top: 12px; width: 200px; height: 116px;
    border-radius: 50%; background: var(--label-white);
    display: flex; align-items: center; justify-content: center;
  }
  .lid-label__photo {
    width: 90px; height: 58px; border-radius: 45%;
    background: radial-gradient(circle at 40% 40%, var(--photo-red), var(--photo-dark));
  }
  .top-divider { position: absolute; top: 20px; bottom: 20px; border-left: 2px dotted var(--white); }
  .top-divider--left { left: 240px; }
  .top-flavour {
    position: absolute; right: 40px; top: 30px;
    font-family: "Oswald", sans-serif; font-weight: 700; font-size: 22px; color: var(--white);
  }
  .paw-icon {
    position: absolute; width: 36px; height: 34px; border-radius: 40%; background: var(--white);
  }
  .paw-icon--top { right: 50px; top: 90px; }

  .headline {
    position: absolute; left: 22px; top: 22px;
    font-family: "Delius", cursive; font-size: 29px; line-height: 1.13; color: var(--ink);
  }
  .headline__accent { color: var(--white); }
  .paw-icon--front { left: 268px; top: 70px; width: 44px; height: 42px; }
  .research-note {
    position: absolute; left: 22px; top: 150px; width: 310px;
    font-family: "Open Sans", sans-serif; font-size: 8.5px; line-height: 1.3; color: var(--ink);
  }
  .flavour {
    position: absolute; left: 390px; top: 28px; text-align: center;
    font-family: "Oswald", sans-serif; color: var(--white);
  }
  .flavour__name { font-weight: 700; font-size: 30px; line-height: 1; }
  .flavour__sub { font-weight: 500; font-size: 12px; }
  .flavour-icon {
    position: absolute; left: 460px; top: 30px; width: 76px; height: 90px;
    border: 3px solid var(--white); border-radius: 40% 40% 45% 45%;
  }
  .benefits {
    position: absolute; left: 580px; top: 30px;
    font-family: "Delius", cursive; font-size: 15px; line-height: 1.3; color: var(--white);
    list-style: none;
  }
  .benefits__lead { color: var(--ink); }
  .claims {
    position: absolute; left: 388px; top: 158px;
    font-family: "Oswald", sans-serif; font-weight: 700; font-style: italic; font-size: 15px;
    letter-spacing: .5px; color: var(--ink);
  }
</style>
</head>
<body>
<div class="canvas">

  <div class="brand-mark">
    <span class="brand-mark__dot"></span>
    <span class="brand-mark__name">Woofloma</span>
  </div>

  <section class="sleeve">
    <div class="sleeve__top">
      <span class="top-brand">Woofloma</span>
      <span class="top-divider top-divider--left"></span>
      <div class="lid-label">
        <div class="lid-label__photo" role="img" aria-label="Photo of a red apple with a green leaf"></div>
      </div>
      <span class="top-flavour">BIBI</span>
      <div class="paw-icon paw-icon--top" role="img" aria-label="Paw print icon"></div>
    </div>

    <div class="sleeve__front">
      <h1 class="headline">Wholesome<br><span class="headline__accent">ALL NATURAL</span><br>treat for dogs.</h1>
      <div class="paw-icon paw-icon--front" role="img" aria-label="Paw print icon"></div>
      <p class="research-note">Current research suggests that apple skin can help protect against some cancers, so we make our Bibi treats with apple skins intact.</p>

      <div class="flavour">
        <div class="flavour__name">BIBI</div>
        <div class="flavour__sub">{APPLE}</div>
      </div>
      <div class="flavour-icon" role="img" aria-label="Apple flavour icon outline"></div>

      <ul class="benefits">
        <li class="benefits__lead">high in</li>
        <li>• vitamin A &amp; B</li>
        <li>• fiber</li>
        <li>+ good way to</li>
        <li>freshen breath</li>
      </ul>

      <p class="claims">100% NATURAL - LOW FAT - LOW CALORIES</p>
    </div>
  </section>

</div>
</body>
</html>
```